VELT MIXER FOR YOUNG BUSINESS PROFESSIONALS

Fresh, Upscale, Classy and Modern. I need some flyer designs for a business mixer coming up for young business professionals. We are targeting business owners and professionals under 40 and we will strive to bridge the gap between successful business owners and young entrepreneurs through hosting striking mixers throughout the year. The flyer needs to have simplicity but at the same time could be abstract or balanced with some complexity or is open to ideas. The event will be hosted at an art gallery. I need something unique and different and good taste but yet creative. Anyone that ends up doing a good job will be rewarded with work for the rest of the year for all of our events. I am open to the usage of colors as long as it looks striking at the end of the day. We can also keep in mind that this flyer can be the jumpstart of a series of different other flyers with variations.
Target Market(s)
Young Business Owners and Professionals under 40
Industry/Entity Type
Events
Requirements
Must have
- Must have space to put who what where when and a spot for a brief catchy title and introduction to possible guest speakers. Must keep in mind that the theme is leadership. The location is TRILK art gallery in Edmonton. Must be able to create a feeling of admiration and inspiration
Nice to have
- nice to have designer that understands and able to balance the designs to make it work. Nice to have something that is completely unique, different and striking but again following the fresh, upscale, classy and modern look.
Should not have
- should not have anything that is typical

```html
<!DOCTYPE html>
<html lang="en">
<head>
<meta charset="utf-8">
<title>VELT Business Mixer</title>
<link href="https://fonts.googleapis.com/css2?family=Arvo:wght@400;700&family=Oswald:wght@500;700&family=Roboto+Condensed:wght@700&display=swap" rel="stylesheet">
<style>
  :root {
    --navy: #23205a;
    --navy-deep: #1a1848;
    --blue: #2f4fa8;
    --blue-mid: #3a5cb8;
    --accent: #2d6fd6;
    --ink: #1d1d1d;
    --grey: #555555;
    --white: #ffffff;
  }
  * { margin: 0; padding: 0; box-sizing: border-box; }
  html, body { width: 849px; height: 1200px; overflow: hidden; background: var(--white); }
  .flyer {
    position: relative;
    width: 849px;
    height: 1200px;
    border: 18px solid var(--navy);
    background: var(--white);
    font-family: "Arvo", serif;
    color: var(--ink);
    text-align: center;
  }
  .invite {
    padding-top: 22px;
    font-family: "Roboto Condensed", sans-serif;
    font-weight: 700;
    font-size: 31px;
    letter-spacing: 0.5px;
    color: var(--navy);
  }
  .invite-rule {
    width: 760px;
    height: 4px;
    margin: 10px auto 0;
    background: var(--accent);
  }
  .brand {
    margin-top: 30px;
    display: flex;
    justify-content: center;
    align-items: flex-start;
    gap: 6px;
    font-family: "Arvo", serif;
    font-weight: 400;
    color: var(--ink);
  }
  .brand-name { font-size: 74px; letter-spacing: 10px; line-height: 1; }
  .brand-suffix { font-size: 18px; margin-top: 6px; }
  .presents { margin-top: 16px; font-size: 24px; color: var(--ink); }

  .banner {
    position: absolute;
    left: 0; right: 0;
    top: 225px;
    height: 394px;
    color: var(--white);
    overflow: hidden;
  }
  .banner-bg {
    position: absolute; inset: 0;
    background: linear-gradient(120deg, var(--blue) 0%, var(--navy) 35%, var(--blue-mid) 60%, var(--navy-deep) 100%);
  }
  .banner-content { position: relative; padding-top: 30px; }
  .tagline {
    font-family: "Oswald", sans-serif;
    font-weight: 500;
    font-size: 30px;
    letter-spacing: 6px;
  }
  .event-title {
    margin-top: 2px;
    font-family: "Oswald", sans-serif;
    font-weight: 700;
    font-size: 84px;
    line-height: 1.05;
    letter-spacing: 2px;
  }
  .speakers {
    margin-top: 18px;
    display: flex;
    justify-content: center;
    align-items: center;
    gap: 48px;
  }
  .speaker-label {
    width: 150px;
    font-family: "Oswald", sans-serif;
    font-weight: 500;
    font-size: 16px;
    line-height: 1.25;
    letter-spacing: 0.5px;
  }
  .speaker-photo {
    width: 98px; height: 98px;
    border-radius: 50%;
    border: 4px solid var(--white);
    background: radial-gradient(circle at 50% 40%, #b89a86 0%, #6d5a55 55%, #3a3a4a 100%);
  }
  .speaker-photo.second { background: radial-gradient(circle at 50% 40%, #c2a58d 0%, #8a7563 55%, #4a4a52 100%); }
  .speaker-with {
    margin-top: 24px;
    font-family: "Oswald", sans-serif;
    font-weight: 500;
    font-size: 17px;
    letter-spacing: 0.5px;
  }
  .speaker-with strong { font-size: 23px; font-weight: 700; }

  .details { position: absolute; left: 0; right: 0; top: 660px; }
  .venue { font-size: 40px; color: var(--ink); }
  .venue strong { font-weight: 700; }
  .address { margin-top: 8px; font-size: 25px; color: var(--ink); }
  .rule { width: 560px; height: 2px; margin: 0 auto; background: #777; }
  .rule.top { margin-top: 20px; }
  .date { margin: 14px 0 10px; font-size: 70px; line-height: 1.1; color: var(--ink); }
  .time { margin-top: 20px; font-size: 28px; color: var(--ink); }
  .rsvp { margin-top: 34px; font-size: 23px; line-height: 1.9; color: var(--grey); }
</style>
</head>
<body>
<main class="flyer">
  <header>
    <p class="invite">INVITING ALL YOUNG PROFESSIONALS</p>
    <div class="invite-rule"></div>
    <div class="brand">
      <span class="brand-name">VELT</span><span class="brand-suffix">inc</span>
    </div>
    <p class="presents">presents</p>
  </header>

  <section class="banner">
    <div class="banner-bg" role="img" aria-label="Abstract geometric pattern of navy and royal blue facets"></div>
    <div class="banner-content">
      <p class="tagline">BRIEF CATCHY TITLE HERE</p>
      <h1 class="event-title">BUSINESS MIXER</h1>
      <div class="speakers">
        <p class="speaker-label">ALTERNATIVE SPACE FOR SPEAKER 1 NAME</p>
        <div class="speaker-photo" role="img" aria-label="Portrait photo of guest speaker 1"></div>
        <div class="speaker-photo second" role="img" aria-label="Portrait photo of guest speaker 2"></div>
        <p class="speaker-label">ALTERNATIVE SPACE FOR SPEAKER 2 NAME</p>
      </div>
      <p class="speaker-with">WITH: <strong>NAME OF SPEAKER/S HERE</strong> (IF ONLY 1 SPEAKER OR MORE THAN 2)</p>
    </div>
  </section>

  <section class="details">
    <p class="venue"><strong>TRILK</strong> Art Gallery</p>
    <p class="address">20456 98 Ave NW, Edmonton, AB T6K 2P4</p>
    <div class="rule top"></div>
    <p class="date">15 October 2015</p>
    <div class="rule"></div>
    <p class="time">06.00 PM - 09.00 PM</p>
    <p class="rsvp">RSVP NOW:<br>info@veltinc.com | Jane Roe: 0712 34567<br>www.veltinc.com</p>
  </section>
</main>
</body>
</html>
```